Label Design Project for my tea product Imported from Japan

I have a tea importing business. I want someone to help me design a label for my Uji matcha tea product. I want the label to be modern, neat, and beautifully designed. I prefer it to be easily adaptable to other tea products that I will be importing.
Product name: Organic Hoshiba Matcha
Company name: Calm Harbor Leaf Merchants
Description: Powdered Green Tea Matcha
Ceremonial grade premium quality
Directly imported from Japan
This product is going to be sold in the U.S. market, so please make sure that the label is in compliance with the BQC regulations.

Target Market(s)

High end tea consumers

Industry/Entity Type

Business

Requirements
Must have
• Marking of origin : product of Japan
• Imported by: Calm Harbor Leaf Merchants
• Leave space for Net weight, the name and place of business of the manufacturer.
• Ingredients: Green Tea 100%
• Nutrition list is not necessary.

```html
<!DOCTYPE html>
<html lang="en">
<head>
<meta charset="utf-8">
<title>Organic Hoshiba Matcha — Label</title>
<link rel="stylesheet" href="https://fonts.googleapis.com/css2?family=Lato:wght@300;400;700;900&display=swap">
<style>
  :root {
    --page: #ffffff;
    --leaf: #2f9b64;
    --leaf-deep: #268a57;
    --mist: #eceeec;
    --ink-soft: #8a8f8c;
    --white: #ffffff;
  }
  * { box-sizing: border-box; margin: 0; padding: 0; }
  html, body { width: 1200px; height: 800px; overflow: hidden; background: var(--page); }
  body { font-family: "Lato", sans-serif; position: relative; }

  .label {
    position: absolute; left: 418px; top: 96px;
    width: 365px; height: 606px;
    background: var(--leaf);
  }

  .brand-tab {
    position: absolute; left: 41px; top: 0;
    width: 282px; height: 142px;
    background: var(--mist);
    border-radius: 0 0 10px 10px;
  }
  .brand-tab::after {
    content: ""; position: absolute; inset: 0 4px 4px 4px;
    border: 1px dashed var(--leaf);
    border-top: none;
    border-radius: 0 0 8px 8px;
  }
  .brand-mark {
    position: absolute; left: 0; right: 0; top: 62px;
    display: flex; align-items: center; justify-content: center; gap: 7px;
    color: var(--ink-soft); font-weight: 300; font-size: 13px; letter-spacing: 0.5px;
  }
  .brand-mark .dot { width: 10px; height: 10px; border-radius: 50%; background: var(--leaf); }
  .brand-name {
    position: absolute; left: 0; right: 0; top: 106px;
    text-align: center; color: var(--leaf);
    font-weight: 900; font-size: 12.5px; letter-spacing: 0.3px;
  }

  .product-title {
    position: absolute; left: 0; right: 0; top: 160px;
    text-align: center; color: var(--white);
    font-weight: 700; font-size: 30px; letter-spacing: -0.2px;
  }

  .facts {
    position: absolute; left: 109px; top: 287px;
    width: 149px; height: 149px;
    border: 2px solid var(--white); border-radius: 8px;
    padding: 3px; background: var(--leaf);
  }
  .facts-inner {
    width: 100%; height: 100%;
    background: var(--mist); border-radius: 5px;
    display: grid; grid-template-rows: 37px 37px 32px 1fr;
  }
  .facts-row {
    display: flex; align-items: center; justify-content: center;
    color: var(--leaf); text-align: center;
    border-bottom: 1px solid var(--leaf);
  }
  .facts-row:last-child { border-bottom: none; }
  .facts-head { font-size: 12px; font-weight: 700; }
  .facts-value { font-size: 16px; font-weight: 400; }

  .footer-band {
    position: absolute; left: 0; top: 512px;
    width: 100%; height: 72px;
    background: var(--mist);
  }
  .cert-mark {
    position: absolute; left: 41px; top: 31px;
    color: var(--leaf); font-weight: 900; font-size: 20px; letter-spacing: 1px;
  }
  .importer {
    position: absolute; left: 228px; top: 10px; width: 112px;
    text-align: center; color: var(--leaf);
  }
  .importer-label { font-size: 7px; font-weight: 700; }
  .importer-mark {
    margin-top: 6px; display: flex; align-items: center; justify-content: center; gap: 3px;
    color: var(--ink-soft); font-size: 6px; font-weight: 300;
  }
  .importer-mark .dot { width: 5px; height: 5px; border-radius: 50%; background: var(--leaf); }
  .importer-name { margin-top: 9px; font-size: 5.5px; font-weight: 900; white-space: nowrap; }
</style>
</head>
<body>
  <main class="label">
    <header class="brand-tab">
      <div class="brand-mark"><span class="dot"></span>Calm Harbor Leaf Merchants</div>
      <div class="brand-name">CALM HARBOR LEAF MERCHANTS</div>
    </header>

    <h1 class="product-title">Organic Hoshiba Matcha</h1>

    <section class="facts">
      <div class="facts-inner">
        <div class="facts-row facts-head">Ingredients :</div>
        <div class="facts-row facts-value">Green Tea 100%</div>
        <div class="facts-row facts-head">Marking of origin :</div>
        <div class="facts-row facts-value">Product of Japan</div>
      </div>
    </section>

    <footer class="footer-band">
      <div class="cert-mark">BQC</div>
      <div class="importer">
        <div class="importer-label">Imported by :</div>
        <div class="importer-mark"><span class="dot"></span>Calm Harbor Leaf Merchants</div>
        <div class="importer-name">CALM HARBOR LEAF MERCHANTS</div>
      </div>
    </footer>
  </main>
</body>
</html>
```